LuMarking-Tagvelory Partial Redesign - Web App

Are you able to apply your creativity to an existing layout? I’m convinced that even just a few touches can make a big difference to add personality and professionalism to a website design, and I’m looking for someone able to use existing ideas and bring them to the next level while keeping inside some given constraints.
The actual job is to improve an existing design concept and to apply it creatively to a landing page, a simple home page, and an older web app (single page website).
To help you start with a clear picture of the current situation and of my requirements, I created a detailed brief with screenshots, live examples, and complete instructions. You can find it attached to this job.
My tastes are inclined towards clean and simple designs. For this project I'm not looking for dazzling novelty, but for very solid craftsmanship. Are the right man - or woman - for the job?
Updates
I wanted to thank everybody who participated in this project. I made a choice, but also other designs were interesting. Hope to work with you another time.
Target Market(s)
Our main target is social media marketers and startuppers
Look and feel
Each slider illustrates characteristics of the customer's brand and the style your logo design should communicate.

```html
<!DOCTYPE html>
<html lang="en">
<head>
<meta charset="utf-8">
<title>Tagvelory – Hashtag Summary</title>
<link href="https://fonts.googleapis.com/css2?family=Ubuntu:ital,wght@0,400;0,500;1,400&display=swap" rel="stylesheet">
<style>
:root{
  --bar:#2a2a2a; --bar-line:#3a3a3a; --bar-text:#ffffff;
  --bg:#ffffff; --soft:#f4f4f4; --ink:#333333; --muted:#777777;
  --link:#2a7ad0; --blue:#2f76cc; --blue-dark:#1a5fb4;
  --red:#dc3912; --orange:#ff9900; --green:#109618; --pie-blue:#3366cc;
  --footer:#2b2b2b; --footer-text:#cfcfcf;
}
*{box-sizing:border-box;margin:0;padding:0}
html,body{width:1125px;height:1200px;overflow:hidden;background:var(--footer)}
.page{width:1350px;height:1440px;transform:scale(.833333);transform-origin:0 0;font-family:"Ubuntu",sans-serif;color:var(--ink);background:var(--bg);position:relative}
.topbar{height:59px;background:var(--bar);position:relative}
.topbar a{position:absolute;top:0;height:59px;line-height:60px;color:var(--bar-text);font-size:13px;text-decoration:none;text-align:center;border-left:1px solid var(--bar-line)}
.nav-home{left:197px;width:130px;background:#1f1f1f}
.nav-products{left:327px;width:130px;border-right:1px solid var(--bar-line)}
.nav-blog{left:676px;width:95px}
.nav-about{left:771px;width:110px}
.nav-help{left:881px;width:100px;border-right:1px solid var(--bar-line)}
.caret{display:inline-block;border:6px solid transparent;border-top:8px solid #ccc;margin-left:8px;vertical-align:-4px}
.user{position:absolute;left:1011px;top:12px;display:flex;gap:12px}
.avatar{width:35px;height:35px;background:#ddd;border:1px solid #999}
.user-name{color:var(--link);font-size:12px;line-height:17px}
.user-out{color:#999;font-size:9px;letter-spacing:.5px}
.header{background:var(--soft);height:125px;border-bottom:1px solid #ddd;position:relative}
.tagbox{position:absolute;left:197px;top:21px;height:45px;display:flex;align-items:center;background:#e8e8e8}
.tagbox h1{font-weight:400;font-size:26px;padding:0 8px;color:#444}
.tagbox h1 span{color:var(--link)}
.tracked{background:#fff;height:45px;line-height:45px;padding:0 18px 0 7px;font-size:14px;color:#777}
.tracked em{color:var(--link)}
.tabs{position:absolute;top:92px;left:193px;display:flex;font-size:14px;color:#444}
.tabs span{padding:7px 13px;margin-right:22px}
.tabs .on{background:#fff;color:var(--link)}
.tabs .wide{margin-right:60px}
.stats{position:absolute;top:218px;left:204px;display:flex;gap:20px}
.stat{height:79px;border:1px solid #ccc;border-radius:3px;background:linear-gradient(#fff,#ececec);padding:10px 15px}
.stat b{display:block;font-weight:400;font-size:27px;color:#444}
.stat i{font-size:13px;color:#888}
.stat.hot{background:linear-gradient(#3c8ae0,#1766c2);border-color:#1a5fb4}
.stat.hot b,.stat.hot i{color:#fff}
.section-bar{position:absolute;left:204px;width:937px;height:50px;border:1px solid #ccc;border-radius:3px;background:linear-gradient(#fff,#e6e6e6);text-align:center;line-height:48px;font-size:17px;font-weight:500;color:#444}
.chart-title{position:absolute;font-size:15px;font-weight:500;color:#333;display:flex;align-items:center;gap:6px;white-space:nowrap}
.person{display:inline-block;width:8px;height:24px;vertical-align:middle}
.chart{position:absolute}
.legend{position:absolute;font-size:11px;color:#222;line-height:14px}
.legend div{display:flex;gap:4px;margin-bottom:4px}
.sw{width:11px;height:11px;flex:none;margin-top:1px}
.footer{position:absolute;left:0;top:1254px;width:1350px;height:186px;background:var(--footer);color:var(--footer-text);font-size:10px}
.brand{position:absolute;left:197px;top:24px;display:flex;align-items:center;gap:8px}
.brand-mark{width:24px;height:24px;border-radius:50%;background:#9a9a9a}
.brand-name{font-size:20px;font-weight:500;color:#9a9a9a;padding-right:10px;border-right:1px solid #777}
.copy{line-height:13px;letter-spacing:.2px}
.terms{position:absolute;left:197px;top:75px;font-size:11px}
.terms u{color:#fff}
.social{position:absolute;left:999px;top:38px;display:flex;align-items:center;gap:4px;font-size:11px}
.social span{margin-right:10px}
.social i{width:20px;height:20px;background:#ddd;border-radius:2px}
</style>
</head>
<body>
<div class="page">
  <nav class="topbar">
    <a class="nav-home">HOME</a>
    <a class="nav-products">PRODUCTS<span class="caret"></span></a>
    <a class="nav-blog">BLOG</a>
    <a class="nav-about">ABOUT</a>
    <a class="nav-help">HELP</a>
    <div class="user"><div class="avatar"></div><div><div class="user-name">IAMTHEUSER</div><div class="user-out">LOGOUT</div></div></div>
  </nav>

  <header class="header">
    <div class="tagbox"><h1>Hashtag:<span>#chirptips</span></h1><div class="tracked">Tracked influencers: <em>@marlowpike, @rubyfernstudio</em></div></div>
    <div class="tabs"><span class="on">Summary</span><span>Timeline</span><span class="wide">Influencers</span><span>Hashtags</span></div>
  </header>

  <div class="stats">
    <div class="stat" style="width:124px"><b>8</b><i>Observed Days</i></div>
    <div class="stat hot" style="width:181px"><b>8,492,949</b><i>Total Impressions</i></div>
    <div class="stat hot" style="width:182px"><b>843</b><i>Total Tweets</i></div>
    <div class="stat" style="width:182px"><b>1,061,619</b><i>Daily Impressions</i></div>
    <div class="stat" style="width:182px"><b>105</b><i>Daily Tweets</i></div>
  </div>

  <div class="section-bar" style="top:334px">TREND ANALYSIS</div>

  <svg width="0" height="0" style="position:absolute">
    <defs>
      <symbol id="person" viewBox="0 0 8 24"><circle cx="4" cy="3" r="3"/><rect x="1" y="7" width="6" height="10" rx="2"/><rect x="2.5" y="16" width="3" height="8"/></symbol>
      <g id="gauge">
        <circle r="133" fill="#d8d8d8" stroke="#999"/>
        <circle r="122" fill="#f7f7f7"/>
        <path d="M-81.3 81.3A115 115 0 0 1-73.9-88.1L-57.9-68.9A90 90 0 0 0-63.6 63.6Z" fill="var(--red)"/>
        <path d="M-73.9-88.1A115 115 0 0 1 57.5-99.6L45-77.9A90 90 0 0 0-57.9-68.9Z" fill="var(--orange)"/>
        <path d="M57.5-99.6A115 115 0 0 1 81.3 81.3L63.6 63.6A90 90 0 0 0 45-77.9Z" fill="var(--green)"/>
        <line x1="0" y1="-115" x2="0" y2="-92" stroke="#333" stroke-width="2"/>
        <line x1="-106" y1="-40" x2="-85" y2="-32" stroke="#333" stroke-width="2"/>
        <line x1="106" y1="-40" x2="85" y2="-32" stroke="#333" stroke-width="2"/>
        <text y="-30" text-anchor="middle" font-size="30" fill="#333">Trend</text>
        <text x="-42" y="64" text-anchor="middle" font-size="16" fill="#333">-100</text>
        <text x="46" y="64" text-anchor="middle" font-size="16" fill="#333">100</text>
        <text y="96" text-anchor="middle" font-size="28" fill="#111">3</text>
        <path d="M3-108L8 0 0 36-6 0Z" fill="#e2654a" stroke="#c0442b"/>
        <circle r="17" fill="#4a86e8" stroke="#3a6fc4"/>
      </g>
    </defs>
  </svg>

  <div class="chart-title" style="left:299px;top:424px">Trend With Your Influencers
    <svg class="person" style="fill:var(--red)"><use href="#person"/></svg><svg class="person" style="fill:var(--red)"><use href="#person"/></svg><svg class="person" style="fill:var(--link)"><use href="#person"/></svg></div>
  <div class="chart-title" style="left:764px;top:424px">Trend Without Your Influencers
    <svg class="person" style="fill:var(--red)"><use href="#person"/></svg><svg class="person" style="fill:var(--red)"><use href="#person"/></svg></div>

  <svg class="chart" role="img" aria-label="Trend gauge with influencers, value 3" style="left:300px;top:476px" width="272" height="272"><use href="#gauge" x="136" y="136"/></svg>
  <svg class="chart" role="img" aria-label="Trend gauge without influencers, value 3" style="left:767px;top:476px" width="272" height="272"><use href="#gauge" x="136" y="136"/></svg>

  <div class="section-bar" style="top:851px">YOUR INFLUENCERS ANALYSIS</div>

  <div class="chart-title" style="left:255px;top:941px">Your Influencers <svg class="person" style="fill:var(--link)"><use href="#person"/></svg> vs Rest Of The Internet
    <svg class="person" style="fill:var(--red)"><use href="#person"/></svg><svg class="person" style="fill:var(--red)"><use href="#person"/></svg></div>
  <div class="chart-title" style="left:746px;top:941px">Your Influencers <svg class="person" style="fill:var(--link)"><use href="#person"/></svg> vs Your Influencers <svg class="person" style="fill:var(--link)"><use href="#person"/></svg></div>

  <svg class="chart" role="img" aria-label="Pie: tracked influencers 14.9%, others 85.1%" style="left:345px;top:1002px" width="180" height="180">
    <g transform="translate(90 90)">
      <circle r="86" fill="var(--red)"/>
      <path d="M0 0V-86A86 86 0 0 1 69.2-51Z" fill="var(--pie-blue)" stroke="#fff"/>
      <text x="28" y="-51" font-size="10" fill="#fff" text-anchor="middle">14.9%</text>
      <text x="-28" y="60" font-size="10" fill="#fff" text-anchor="middle">85.1%</text>
    </g>
  </svg>
  <div class="legend" style="left:539px;top:998px">
    <div><span class="sw" style="background:var(--pie-blue)"></span><span>Tracked<br>Influencers</span></div>
    <div><span class="sw" style="background:var(--red)"></span><span>Others</span></div>
  </div>

  <svg class="chart" role="img" aria-label="Pie: rubyfernstudio 8.1%, marlowpike 91.9%" style="left:812px;top:1002px" width="180" height="180">
    <g transform="translate(90 90)">
      <circle r="86" fill="var(--red)"/>
      <path d="M0 0V-86A86 86 0 0 1 42-75Z" fill="var(--pie-blue)" stroke="#fff"/>
      <text x="16" y="-60" font-size="10" fill="#fff" text-anchor="middle">8.1%</text>
      <text x="-17" y="67" font-size="10" fill="#fff" text-anchor="middle">91.9%</text>
    </g>
  </svg>
  <div class="legend" style="left:1006px;top:998px">
    <div><span class="sw" style="background:var(--pie-blue)"></span><span>rubyfernst...</span></div>
    <div><span class="sw" style="background:var(--red)"></span><span>marlowpike</span></div>
  </div>

  <footer class="footer">
    <div class="brand"><span class="brand-mark"></span><span class="brand-name">LuMarking</span>
      <div class="copy">COPYRIGHT © 2011-2012 LUMARKING LTD.<br>48 Quarry Lane N7 4QD Eastbury, UK</div></div>
    <div class="terms">Use of this website constitutes acceptance of our <u>User Agreement</u> and <u>Privacy Policy</u></div>
    <div class="social"><span>Stay Connected</span><i></i><i></i><i></i></div>
  </footer>
</div>
</body>
</html>
```